Australian Online Training Organisation needs a Website Design

We need a Web Design ideally using a Wordpress Divi template which will represent an Australian Online Training Company.

(Harlow Net Learning)

The website will represent a range of short courses with an emphasis on business, zentrosoft, leadership etc.

The website will 'shell out' to the third party portal where 'bookings' occur. I am imaging a fantastic looking web design with perhaps 5-6 pages.

I am wondering if a selection of courses including the below list can be incorporated?

The variety of courses include :

Workplace Safety
Sales Training
Leadership
Process Management
Problem Solving
Project Management
Business Planning
Meetings and Events
Emotional Intelligence
Human Resources
Administrative Essentials
Customer Service
Career Development
Conflict Resolution
Train the Trainer
Supervisors and Managers
Internet marketing
Communications
Team Building
Marketing
Finance
Writing
Job Search Skills
Public Speaking
Negotiation Skills
Talent Management
Zentrosoft Deskline 2016
ZDC Preparation for Office 2010
Office 2013
Office 2010
Upgrading to Office 2010
Computer Fundamentals
Upgrading to Office 2007
Office 2003
Office 2002
Pavra Suite X3
Core Essentials
Office 2007

Thank you so much for all of the amazing designs we received. We were so happy with so many elements that it was very hard to choose. Our top two were very hard to decide upon but we look forward to working more with both of these talents into the future. Thank you again.

Target Market(s)

Professionals, students and workers who would like to improve their skills with online training in over 500 + courses -

Industry/Entity Type

It Company

Number of Pages Required

5+ page

Font styles to use
Sans Serif

Colors
3276b5
faa54b
0355a3
fac994

Requirements
Must have
• Ideally would use Wordpress theme (Divi for example or other)
• Very smart front end
• Will upload logo soon
• (Harlow Net Learning)
• harlownetlearning.edu.au
• Graphics of 'people' pretty important - with a variety of ages.
Nice to have
• Interesting page
• National presence
• A bit University looking
• Professional
• Graphics of people
• Blog
• Graphics of people
• Age range from job seekers, to business folk, etc

```html
<!DOCTYPE html>
<html lang="en">
<head>
<meta charset="utf-8">
<title>Harlow Net Learning</title>
<link href="https://fonts.googleapis.com/css2?family=Open+Sans:ital,wght@0,400;0,600;0,700;1,400&family=Roboto:wght@300;400;500&family=Roboto+Condensed:wght@400;700&display=swap" rel="stylesheet">
<style>
:root{
  --navy:#0355a3;
  --blue:#3276b5;
  --sky:#1a7bc4;
  --orange:#faa54b;
  --orange-deep:#f4933a;
  --peach:#fac994;
  --deep:#0a3f96;
  --ink:#333;
  --muted:#666;
  --light:#f3f3f3;
  --dark:#2b2b2b;
  --white:#fff;
}
*{margin:0;padding:0;box-sizing:border-box}
html,body{width:1200px;height:2853px;overflow:hidden}
body{font-family:"Open Sans",sans-serif;color:var(--ink);background:var(--white);position:relative}
.abs{position:absolute}
.heading{font-family:"Roboto Condensed",sans-serif;font-weight:400;text-transform:uppercase}

/* header */
.site-header{position:absolute;left:0;top:0;width:1200px;height:156px;background:var(--white);z-index:3}
.brand-tab{position:absolute;left:70px;top:0;width:210px;height:190px;background:var(--white);border-radius:0 0 105px 105px/0 0 40px 40px;z-index:4;text-align:center;padding-top:26px}
.brand-dot{width:58px;height:58px;border-radius:50%;background:var(--navy);margin:0 auto 10px}
.brand-name{font-family:"Roboto Condensed",sans-serif;font-weight:700;color:var(--navy);font-size:25px;line-height:28px;text-transform:uppercase}
.call{position:absolute;left:561px;top:30px;font-size:14px;line-height:22px;color:var(--ink)}
.call-icon{position:absolute;left:-42px;top:4px}
.search{position:absolute;left:852px;top:32px;width:248px;height:40px;border:1px solid #ddd;border-radius:3px;font-size:12px;color:#555;padding:11px 14px}
.search svg{position:absolute;right:14px;top:13px}
.main-nav{position:absolute;left:358px;top:105px;width:842px;height:51px;background:var(--navy);display:flex;align-items:center}
.main-nav::before{content:"";position:absolute;left:0;top:0;width:118px;height:51px;background:var(--dark);clip-path:polygon(30px 0,100% 0,100% 100%,0 100%)}
.main-nav a{position:relative;color:var(--white);font-family:"Roboto Condensed",sans-serif;font-size:14px;text-decoration:none;text-transform:uppercase;margin-right:30px}
.main-nav a:first-child{margin-left:62px;margin-right:52px}

/* hero */
.hero{position:absolute;left:0;top:156px;width:1200px;height:515px;background:linear-gradient(100deg,#c9cdd2 0%,#e8eaec 35%,#dfe3e7 60%,#b8c0c9 100%)}
.hero-title{position:absolute;left:0;width:1200px;top:74px;text-align:center;font-size:50px;color:var(--navy)}
.hero-arrow{position:absolute;top:240px}

/* courses */
.courses{position:absolute;left:0;top:671px;width:1200px;height:438px}
.section-title{position:absolute;left:0;width:1200px;top:42px;text-align:center;font-size:32px;color:var(--ink)}
.title-rule{position:absolute;left:563px;top:96px}
.course{position:absolute;top:136px;width:230px;text-align:center}
.course-icon{width:114px;height:114px;border-radius:50%;margin:0 auto;display:flex;align-items:center;justify-content:center;background:var(--navy)}
.course-icon.orange{background:#d87b1f}
.course-name{font-family:"Roboto",sans-serif;font-size:15px;text-transform:uppercase;margin-top:22px;color:var(--ink)}
.course-text{font-size:11.5px;line-height:20px;color:var(--muted);margin-top:8px}
.course-more{margin-top:14px}
.side-arrow{position:absolute;top:220px}

/* welcome */
.welcome{position:absolute;left:0;top:1109px;width:1200px;height:447px;background:linear-gradient(90deg,#ececec 0%,#f6f6f6 60%,#e9eaeb 100%)}
.welcome-photo{position:absolute;left:760px;top:0;width:440px;height:447px;background:linear-gradient(120deg,#e6e9ec 0%,#9fb6cf 45%,#5d86b8 75%,#d9dde1 100%)}
.welcome-kicker{position:absolute;left:106px;top:76px;font-size:27px;color:var(--ink)}
.welcome-title{position:absolute;left:106px;top:112px;font-size:39px;color:var(--ink)}
.welcome-copy{position:absolute;left:106px;top:172px;width:505px;font-size:12.5px;line-height:21px;color:#444}
.welcome-copy p{margin-bottom:12px}
.btn-dark{position:absolute;left:106px;top:348px;width:124px;height:32px;background:var(--dark);color:var(--white);font-family:"Roboto",sans-serif;font-size:12.5px;text-transform:uppercase;display:flex;align-items:center;justify-content:center;border-radius:2px}

/* features */
.feature{position:absolute;top:1556px;width:600px;height:188px;color:var(--white)}
.feature.flexible{left:0;background:linear-gradient(120deg,#2186cf,#1570b8)}
.feature.value{left:599px;width:601px;background:linear-gradient(120deg,#f9a447,#f38e33)}
.feature-ring{position:absolute;left:106px;top:41px;width:100px;height:100px;border:2px solid var(--white);border-radius:50%;display:flex;align-items:center;justify-content:center}
.feature.value .feature-ring{left:29px}
.feature-title{position:absolute;left:224px;top:30px;font-size:27px}
.feature.value .feature-title{left:158px}
.feature-text{position:absolute;left:224px;top:74px;width:340px;font-size:11.5px;line-height:20px}
.feature.value .feature-text{left:158px;width:360px}
.feature-link{position:absolute;left:224px;top:142px;font-size:11.5px;text-transform:uppercase;display:flex;align-items:center;gap:8px}
.feature.value .feature-link{left:158px}

/* new courses */
.new-title{position:absolute;left:97px;top:1794px;font-size:25px;color:var(--ink)}
.card{position:absolute;top:1843px;width:312px}
.card-media{width:312px;height:171px;position:relative}
.card-media .play{position:absolute;left:136px;top:66px}
.card-title{font-family:"Roboto",sans-serif;font-weight:300;font-size:20px;color:var(--navy);margin-top:14px}
.card-text{font-size:11.5px;line-height:21px;color:#555;margin-top:4px}

/* testimonial */
.testimonial{position:absolute;left:0;top:2187px;width:1200px;height:213px;background:var(--deep)}
.testimonial-label{position:absolute;left:97px;top:90px;font-size:32px;color:var(--white)}
.testimonial-photo{position:absolute;left:341px;top:48px;width:110px;height:110px;border-radius:50%;border:4px solid var(--white);background:radial-gradient(circle at 50% 40%,#e9c7a6,#b88664 60%,#6a4a36)}
.quote{position:absolute;left:476px;top:44px;width:630px;font-size:12.5px;line-height:22px;font-style:italic;color:var(--white)}
.quote-by{position:absolute;left:476px;top:136px;font-size:15px;font-style:italic;color:var(--white)}
.quote-nav{position:absolute;left:474px;top:168px;display:flex;gap:3px}

/* partners */
.partners{position:absolute;left:0;top:2400px;width:1200px;height:139px;display:flex;align-items:center;justify-content:center;gap:52px}
.partner{font-family:"Open Sans",sans-serif;font-weight:700;font-size:32px}

/* footer */
.site-footer{position:absolute;left:0;top:2539px;width:1200px;height:257px;background:var(--light)}
.footer-brand{position:absolute;left:95px;top:50px;width:180px;text-align:center}
.footer-col{position:absolute;top:48px}
.footer-col h4{font-family:"Roboto",sans-serif;font-weight:400;font-size:15px;text-transform:uppercase;color:var(--ink);margin-bottom:14px}
.footer-col li{list-style:none;font-size:11.5px;line-height:25.5px;color:#444}
.footer-col p{font-size:11.5px;line-height:20px;color:#444}
.field{width:262px;height:40px;background:var(--white);border:1px solid #ddd;font-size:11.5px;padding:11px 14px;color:#333}
.subscribe{position:absolute;left:161px;top:0;width:101px;height:42px;background:var(--navy);color:var(--white);font-size:12px;text-transform:uppercase;display:flex;align-items:center;justify-content:center}
.contact-line{display:flex;align-items:center;gap:14px;font-size:12px;color:#444;margin-top:8px}
.bottom-bar{position:absolute;left:0;top:2796px;width:1200px;height:57px;background:var(--light)}
.bottom-bar .band{position:absolute;left:266px;top:0;width:934px;height:57px;background:var(--navy);clip-path:polygon(40px 0,100% 0,100% 100%,0 100%)}
.copyright{position:absolute;left:327px;top:20px;font-size:11.5px;color:var(--white)}
.social{position:absolute;left:962px;top:16px;display:flex;gap:6px}
.social span{width:24px;height:24px;border:1.5px solid var(--white);border-radius:50%}
</style>
</head>
<body>

<header class="site-header">
  <div class="call">
    <svg class="call-icon" width="34" height="34" viewBox="0 0 34 34"><circle cx="17" cy="17" r="15.5" fill="none" stroke="#0355a3" stroke-width="2"/><path d="M12 10c1-1 2 0 3 2s0 2-1 3c1 2 2 3 4 4 1-1 2-2 3-1s3 2 2 3c-1 2-3 2-5 1-3-2-5-4-7-7-1-2-1-4 1-5z" fill="#0355a3"/></svg>
    Call Us : +1 555 - 210 - 3390<br>info@harlownetlearning.edu.au
  </div>
  <div class="search">Search Here
    <svg width="14" height="14" viewBox="0 0 14 14"><circle cx="6" cy="6" r="4.5" fill="none" stroke="#222" stroke-width="2"/><path d="M9.5 9.5l3.5 3.5" stroke="#222" stroke-width="2"/></svg>
  </div>
  <nav class="main-nav">
    <a>Home</a><a>About Us</a><a>Courses</a><a>Employers</a><a>Support &amp; Resources</a><a>Blog</a><a>Contact Us</a>
  </nav>
</header>

<div class="brand-tab">
  <div class="brand-dot"></div>
  <div class="brand-name">Harlow Net Learning</div>
</div>

<section class="hero" role="img" aria-label="Photo of a group of young professionals at a meeting table watching a presenter on a video call screen">
  <h1 class="hero-title heading">Harlow Net Learning</h1>
  <svg class="hero-arrow" style="left:40px" width="16" height="30" viewBox="0 0 16 30"><path d="M14 2L3 15l11 13" fill="none" stroke="#fff" stroke-width="2"/></svg>
  <svg class="hero-arrow" style="left:1144px" width="16" height="30" viewBox="0 0 16 30"><path d="M2 2l11 13L2 28" fill="none" stroke="#fff" stroke-width="2"/></svg>
</section>

<section class="courses">
  <h2 class="section-title heading">Our Courses</h2>
  <svg class="title-rule" width="74" height="12" viewBox="0 0 74 12"><line x1="0" y1="6" x2="74" y2="6" stroke="#555" stroke-width="1.5"/><circle cx="5" cy="6" r="4" fill="#fff" stroke="#555" stroke-width="1.5"/><circle cx="37" cy="6" r="4" fill="#fff" stroke="#555" stroke-width="1.5"/><circle cx="69" cy="6" r="4" fill="#fff" stroke="#555" stroke-width="1.5"/></svg>
  <svg class="side-arrow" style="left:48px" width="22" height="48" viewBox="0 0 22 48"><path d="M20 2L3 24l17 22" fill="none" stroke="#777" stroke-width="1.5"/></svg>
  <svg class="side-arrow" style="left:1128px" width="22" height="48" viewBox="0 0 22 48"><path d="M2 2l17 22L2 46" fill="none" stroke="#777" stroke-width="1.5"/></svg>

  <div class="course" style="left:90px">
    <div class="course-icon orange"><svg width="40" height="46" viewBox="0 0 40 46"><path d="M20 2l17 6v14c0 11-8 19-17 22C11 41 3 33 3 22V8z" fill="#fff"/><path d="M20 8v30c-6-3-11-8-11-16V12z" fill="#d87b1f"/></svg></div>
    <div class="course-name">Workplace Safety</div>
    <p class="course-text">Nemo enim ipsam voluptatem quia volut sit aspernatur aut odit aut fugit, sed quia consequuntur magni dolores</p>
    <svg class="course-more" width="14" height="14" viewBox="0 0 14 14"><path d="M2 2l5 4 5-4M2 8l5 4 5-4" fill="none" stroke="#444" stroke-width="1.8"/></svg>
  </div>
  <div class="course" style="left:357px">
    <div class="course-icon"><svg width="50" height="44" viewBox="0 0 50 44"><rect x="2" y="2" width="46" height="30" rx="3" fill="#fff"/><rect x="6" y="6" width="38" height="22" fill="#0355a3"/><rect x="20" y="32" width="10" height="6" fill="#fff"/><rect x="13" y="38" width="24" height="4" rx="1" fill="#fff"/></svg></div>
    <div class="course-name">Process Management</div>
    <p class="course-text">Nemo enim ipsam voluptatem quia volut sit aspernatur aut odit aut fugit, sed quia consequuntur magni dolores</p>
    <svg class="course-more" width="14" height="14" viewBox="0 0 14 14"><path d="M2 2l5 4 5-4M2 8l5 4 5-4" fill="none" stroke="#444" stroke-width="1.8"/></svg>
  </div>
  <div class="course" style="left:619px">
    <div class="course-icon"><svg width="40" height="42" viewBox="0 0 40 42"><circle cx="20" cy="11" r="9" fill="#fff"/><path d="M3 40c0-11 7-17 17-17s17 6 17 17z" fill="#fff"/></svg></div>
    <div class="course-name">Leadership</div>
    <p class="course-text">Nemo enim ipsam voluptatem quia volut sit aspernatur aut odit aut fugit, sed quia consequuntur magni dolores</p>
    <svg class="course-more" width="14" height="14" viewBox="0 0 14 14"><path d="M2 2l5 4 5-4M2 8l5 4 5-4" fill="none" stroke="#444" stroke-width="1.8"/></svg>
  </div>
  <div class="course" style="left:878px">
    <div class="course-icon"><svg width="44" height="44" viewBox="0 0 44 44"><path d="M6 14h10a5 5 0 1 1 10 0h10v10a5 5 0 1 1 0 10v8H26a5 5 0 1 0-10 0H6V32a5 5 0 1 0 0-10z" fill="#fff"/></svg></div>
    <div class="course-name">Business Planning</div>
    <p class="course-text">Nemo enim ipsam voluptatem quia volut sit aspernatur aut odit aut fugit, sed quia consequuntur magni dolores</p>
    <svg class="course-more" width="14" height="14" viewBox="0 0 14 14"><path d="M2 2l5 4 5-4M2 8l5 4 5-4" fill="none" stroke="#444" stroke-width="1.8"/></svg>
  </div>
</section>

<section class="welcome">
  <div class="welcome-photo" role="img" aria-label="Photo of a smiling man and woman working together at a laptop in a bright office"></div>
  <div class="welcome-kicker heading">Welcome to</div>
  <h2 class="welcome-title heading">Harlow Net Learning</h2>
  <div class="welcome-copy">
    <p>Harlow Net Learning is one of Australia&#39;s leading provider of flexible and affordable online continuing professional development programs, with over 600 online courses now available. Our range of self-paced online courses are delivered completely online via our e-learning system 24/7.</p>
    <p>We offer a range of popular online courses in accounting, finance, bookkeeping, management, marketing, information technology, project management and more. Our online courses are industry relevant and are designed to help you achieve your career goals.</p>
  </div>
  <div class="btn-dark">Read More</div>
</section>

<section class="feature flexible">
  <div class="feature-ring"><svg width="44" height="44" viewBox="0 0 44 44"><path d="M20 4a18 18 0 1 0 18 20H20z" fill="#fff"/><path d="M24 2v18h18A18 18 0 0 0 24 2z" fill="#fff"/></svg></div>
  <h3 class="feature-title heading">Flexible</h3>
  <p class="feature-text">Harlow provide an online learning platform which fits into your lifestyle and work commitments. You study anywhere, anytime! ratione voluptatem sequi nesciunt.</p>
  <div class="feature-link">Click Here <svg width="12" height="12" viewBox="0 0 12 12"><circle cx="6" cy="6" r="6" fill="#fff"/><path d="M5 3l3 3-3 3" fill="none" stroke="#1a7bc4" stroke-width="1.6"/></svg></div>
</section>
<section class="feature value">
  <div class="feature-ring"><svg width="50" height="40" viewBox="0 0 50 40"><circle cx="25" cy="10" r="7" fill="#fff"/><path d="M12 38c0-10 6-15 13-15s13 5 13 15z" fill="#fff"/><circle cx="10" cy="14" r="5" fill="#fff"/><path d="M0 34c0-7 4-11 10-11 2 0 3 0 4 1-2 3-3 6-3 10z" fill="#fff"/><circle cx="40" cy="14" r="5" fill="#fff"/><path d="M50 34c0-7-4-11-10-11-2 0-3 0-4 1 2 3 3 6 3 10z" fill="#fff"/></svg></div>
  <h3 class="feature-title heading">Value</h3>
  <p class="feature-text">Our innovative online training approach allows us to deliver exceptional training in over 600 industry endorsed courses at affordable prices with no hidden extras.</p>
  <div class="feature-link">Click Here <svg width="12" height="12" viewBox="0 0 12 12"><circle cx="6" cy="6" r="6" fill="#fff"/><path d="M5 3l3 3-3 3" fill="none" stroke="#f4933a" stroke-width="1.6"/></svg></div>
</section>

<h2 class="new-title heading">New Courses</h2>
<article class="card" style="left:97px">
  <div class="card-media" role="img" aria-label="Video still of a presenter in a suit at a flip chart with colleagues" style="background:linear-gradient(110deg,#d8dde2,#8a9bb0 55%,#2f3d52)">
    <svg class="play" width="40" height="40" viewBox="0 0 40 40"><circle cx="20" cy="20" r="19" fill="rgba(0,0,0,.45)" stroke="#fff" stroke-width="1.5"/><path d="M16 12l12 8-12 8z" fill="#fff"/></svg>
  </div>
  <h3 class="card-title">Business Planning</h3>
  <p class="card-text">Lorem ipsum dolor sit amet, consectetur adipisicing elit, sed do eiusmod tempor incididunt ut labore et dolore magna aliqua. Ut enim ad minim veniam,</p>
</article>
<article class="card" style="left:443px">
  <div class="card-media" role="img" aria-label="Video still of hands around a table with colourful social media cut-outs and a tablet" style="background:linear-gradient(120deg,#b07a55,#43a7a8 45%,#d9844c 75%,#6b4a36)">
    <svg class="play" width="40" height="40" viewBox="0 0 40 40"><circle cx="20" cy="20" r="19" fill="rgba(0,0,0,.45)" stroke="#fff" stroke-width="1.5"/><path d="M16 12l12 8-12 8z" fill="#fff"/></svg>
  </div>
  <h3 class="card-title">Internet marketing</h3>
  <p class="card-text">Lorem ipsum dolor sit amet, consectetur adipisicing elit, sed do eiusmod tempor incididunt ut labore et dolore magna aliqua. Ut enim ad minim veniam,</p>
</article>
<article class="card" style="left:791px">
  <div class="card-media" role="img" aria-label="Video still of a businessman sitting on steps using a laptop and phone" style="background:linear-gradient(110deg,#9aa3ad,#c9ced3 40%,#2c4a7a 70%,#8d949b)">
    <svg class="play" width="40" height="40" viewBox="0 0 40 40"><circle cx="20" cy="20" r="19" fill="rgba(0,0,0,.45)" stroke="#fff" stroke-width="1.5"/><path d="M16 12l12 8-12 8z" fill="#fff"/></svg>
  </div>
  <h3 class="card-title">Emotional Intelligence</h3>
  <p class="card-text">Lorem ipsum dolor sit amet, consectetur adipisicing elit, sed do eiusmod tempor incididunt ut labore et dolore magna aliqua. Ut enim ad minim veniam,</p>
</article>

<section class="testimonial">
  <h2 class="testimonial-label heading">Testimonial</h2>
  <div class="testimonial-photo" role="img" aria-label="Round portrait of a happy student"></div>
  <p class="quote">&ldquo; Nemo enim ipsam voluptatem quia voluptas sit aspernatur aut odit aut fugit, sed quia consequuntur magni dolores eos qui ratione voluptatem sequi nesciunt. Neque porro quisquam est, qui dolorem ipsum quia dolor sit amet, consectetur, adipisci velit, sed quia non numquam eius</p>
  <div class="quote-by">Sam Porter - Harlow Net Learning</div>
  <div class="quote-nav">
    <svg width="14" height="14" viewBox="0 0 14 14"><circle cx="7" cy="7" r="7" fill="#fff"/><path d="M8 4L5 7l3 3" fill="none" stroke="#0a3f96" stroke-width="1.6"/></svg>
    <svg width="14" height="14" viewBox="0 0 14 14"><circle cx="7" cy="7" r="7" fill="#fff"/><path d="M6 4l3 3-3 3" fill="none" stroke="#0a3f96" stroke-width="1.6"/></svg>
  </div>
</section>

<section class="partners">
  <span class="partner" style="color:#d62129">Brenmark</span>
  <span class="partner" style="color:#1c6b8c">Coralis</span>
  <span class="partner" style="color:#4d148c">Parcelon</span>
  <span class="partner" style="color:#1f4b9a">Movenza</span>
  <span class="partner" style="color:#ee6a1f">Buildhaus</span>
</section>

<footer class="site-footer">
  <div class="footer-brand">
    <div class="brand-dot"></div>
    <div class="brand-name">Harlow Net Learning</div>
  </div>
  <div class="footer-col" style="left:331px">
    <h4>Information</h4>
    <ul>
      <li>Emotional Intelligence</li><li>Human Resources</li><li>Administrative Essentials</li><li>Customer Service</li><li>Career Development</li><li>Conflict Resolution</li>
    </ul>
  </div>
  <div class="footer-col" style="left:533px">
    <h4>Sign Up for Newsletter</h4>
    <p style="width:260px">Excepteur sint occaecat cupidatat non proident, sunt in culpa qui officia deserunt</p>
    <div class="field" style="margin-top:16px">Enter Name</div>
    <div style="position:relative;margin-top:10px">
      <div class="field" style="width:161px">Enter Email</div>
      <div class="subscribe">Subscribe</div>
    </div>
  </div>
  <div class="footer-col" style="left:852px">
    <h4>Contact Us</h4>
    <p>Harlow Net Learning<br>48 Linden Row, Ashford</p>
    <div class="contact-line" style="margin-top:14px"><svg width="16" height="16" viewBox="0 0 16 16"><path d="M3 1c1-1 2 0 3 2s0 2-1 3c1 2 3 4 5 5 1-1 2-2 3-1s3 2 2 3c-1 2-3 2-5 1C6 12 4 10 2 7 1 5 1 3 3 1z" fill="#f4933a"/></svg>+(613) 555-0147</div>
    <div class="contact-line"><svg width="16" height="12" viewBox="0 0 16 12"><rect x="1" y="1" width="14" height="10" fill="none" stroke="#f4933a" stroke-width="1.5"/><path d="M1 1l7 6 7-6" fill="none" stroke="#f4933a" stroke-width="1.5"/></svg>info@harlownetlearning.edu.au</div>
  </div>
</footer>
<div class="bottom-bar">
  <div class="band"></div>
  <div class="copyright">&copy;2015 - 2016 &nbsp;HARLOW NET LEARNING., All Rights Reserved.</div>
  <div class="social"><span></span><span></span><span></span><span></span><span></span><span></span></div>
</div>

</body>
</html>
```